New Peanut Butter Brand Needs Product Label

We need a packaging label for a new to market peanut butter product based in the UK. The range of peanut butters will include a range of great flavours. We have been looking at labels to give inspiration and we are liking the less complicated designs that are on a white background (Sample designs are attached).

The company is called 'Breezy Acorn Company' The name could be used in full or shortened to 'Breezy Acorn Co'

The design should be a little fun and cool (not in a childish way), using bright colours and a mixture of fonts would be fine (as long as the text is easy to read)

For the purposes of this design brief text that should be added to the front of the design is

Brand name (As above)
Sea Salt (The flavour of this product)
Chunky (Peanut butter is chunky or smooth right !!)

Allowance should be given for the ingredients panel and standard information used on a food product.

Key phrases that could be used in the design are below

Great source of protein
Heart Healthy
Packed with nutrients

The food container will be a plastic pot and so the labels are slightly curved. I have attached a picture of a similar pot and a label outline an sizing which should be of help.

```html
<!DOCTYPE html>
<html lang="en">
<head>
<meta charset="utf-8">
<title>Breezy Acorn Co – Sea Salt Chunky Label</title>
<link rel="stylesheet" href="https://fonts.googleapis.com/css2?family=Cabin:wght@700&family=Oswald:wght@500&family=Playfair+Display:wght@400&display=swap">
<style>
  :root {
    --paper: #ffffff;
    --ink: #111111;
    --outline: #222222;
    --brand-red: #e8443a;
    --accent-green: #3cb54a;
    --wave-tan: #b9a46e;
    --flavour-text: #ffffff;
  }
  html, body {
    margin: 0;
    padding: 0;
    overflow: hidden;
    background: var(--paper);
  }
  .label {
    position: relative;
    width: 1200px;
    height: 523px;
    background: var(--paper);
    overflow: hidden;
  }
  .label-outline {
    position: absolute;
    inset: 0;
  }
  .ornament-diamonds {
    position: absolute;
    left: 495px;
    top: 76px;
    width: 255px;
    height: 18px;
    background: var(--ink);
    border-radius: 9px;
  }
  .centre-line {
    position: absolute;
    left: 0;
    width: 1290px;
    margin: 0;
    text-align: center;
    line-height: 1;
  }
  .brand-name {
    top: 150px;
    font-family: "Cabin", sans-serif;
    font-weight: 700;
    font-size: 62px;
    letter-spacing: 1px;
    color: var(--brand-red);
  }
  .texture-name {
    top: 250px;
    font-family: "Oswald", sans-serif;
    font-weight: 500;
    font-size: 46px;
    letter-spacing: 3px;
    color: var(--accent-green);
  }
  .ornament-waves {
    position: absolute;
    left: 492px;
    top: 362px;
    width: 304px;
    height: 38px;
    background: linear-gradient(180deg, rgba(185,164,110,0.55), var(--wave-tan), rgba(185,164,110,0.55));
    border-radius: 6px;
  }
  .flavour-tag {
    position: absolute;
    left: 544px;
    top: 424px;
    width: 199px;
    height: 57px;
    background: var(--ink);
    display: flex;
    align-items: center;
    justify-content: center;
    font-family: "Playfair Display", serif;
    font-size: 34px;
    color: var(--flavour-text);
  }
</style>
</head>
<body>
  <main class="label">
    <svg class="label-outline" width="1200" height="523" viewBox="0 0 1200 523" aria-hidden="true">
      <path d="M2 35 H373 Q599 -30 825 35 H1198 V521 H2 Z" fill="none" stroke="var(--outline)" stroke-width="2"/>
    </svg>

    <div class="ornament-diamonds" role="img" aria-label="Row of small black diamond ornaments"></div>

    <h1 class="centre-line brand-name">BREEZY ACORN CO.</h1>
    <p class="centre-line texture-name">CHUNKY</p>

    <div class="ornament-waves" role="img" aria-label="Three tan wavy line ornaments"></div>

    <div class="flavour-tag">Sea Salt</div>
  </main>
</body>
</html>
```